Business cards for Tile Contractor
Brisk Grout Studio
LAST MINUTE ADDITION TO BUSINESS CARD!!
website address: briskgroutstudio.net
and a space after the area code in phone number:
thanks!!
#85 is closest to what im looking for. Thanks for all the drafts! good stuff!
looks good so far. would like to see more with all the info on the card.

```html
<!DOCTYPE html>
<html lang="en">
<head>
<meta charset="utf-8">
<title>Brisk Grout Studio – Business Cards</title>
<link href="https://fonts.googleapis.com/css2?family=Open+Sans:ital,wght@0,400;0,600;0,700;0,800;1,400&display=swap" rel="stylesheet">
<style>
  :root {
    --stage: #e9e6e2;
    --card: #ffffff;
    --navy: #1c2d4f;
    --ink: #2a2a2a;
    --band-light: #4cb3e6;
    --band-dark: #0f6fae;
    --band-text: #ffffff;
    --muted: #c9c9c9;
  }
  * { margin: 0; padding: 0; box-sizing: border-box; }
  html, body {
    width: 1200px; height: 398px; overflow: hidden;
    background: var(--stage);
    font-family: "Open Sans", Arial, sans-serif;
  }
  .stage {
    position: relative; width: 1200px; height: 398px;
  }
  .card {
    position: absolute; top: 48px;
    width: 535px; height: 305px;
    background: var(--card);
    box-shadow: 0 3px 10px rgba(0,0,0,0.25);
    overflow: hidden;
  }
  .card--front { left: 50px; }
  .card--back  { left: 615px; }

  .brand {
    position: absolute; left: 0; right: 0;
    display: flex; align-items: center; justify-content: center; gap: 12px;
  }
  .brand__mark {
    width: 40px; height: 40px; border-radius: 50%;
    background: var(--navy);
  }
  .brand__name {
    font-weight: 800; font-size: 30px; letter-spacing: 0.5px;
    color: var(--navy); text-transform: uppercase; line-height: 1;
  }
  .card--front .brand { top: 42px; }
  .card--back .brand  { top: 60px; }

  .band {
    position: absolute; left: 0; right: 0; top: 140px; height: 100px;
    background: linear-gradient(180deg, var(--band-light) 0%, var(--band-dark) 100%);
  }
  .band::after {
    content: ""; position: absolute; left: 0; right: 0; bottom: -6px; height: 6px;
    background: linear-gradient(180deg, rgba(15,111,174,0.35), rgba(15,111,174,0));
  }
  .owner {
    position: absolute; left: 255px; right: 20px; top: 160px;
    text-align: center; color: var(--band-text);
  }
  .owner__name  { font-weight: 700; font-size: 17px; }
  .owner__title { font-size: 13px; margin-top: 2px; }

  .contact {
    position: absolute; left: 255px; right: 12px; top: 258px;
    text-align: center; color: var(--ink); font-size: 12px; line-height: 17px;
  }

  .pitch {
    position: absolute; left: 0; right: 0; top: 170px;
    text-align: center; color: var(--ink);
  }
  .pitch__quote { font-size: 18px; font-style: italic; }
  .pitch__line  { font-size: 16px; margin-top: 4px; }
  .pitch__web   { font-size: 14px; margin-top: 8px; color: var(--band-dark); }
</style>
</head>
<body>
<main class="stage">
  <section class="card card--front" aria-label="Front of business card">
    <div class="brand">
      <span class="brand__mark"></span>
      <span class="brand__name">Brisk Grout Studio</span>
    </div>
    <div class="band"></div>
    <div class="owner">
      <p class="owner__name">Reno Calder</p>
      <p class="owner__title">Owner/Tile Setter</p>
    </div>
    <div class="contact">
      <p>2210 W. Harbor Ln, Marisol, CA 90210</p>
      <p>P: (555) 014-2270 E: briskgroutstudio@mail.com</p>
    </div>
  </section>

  <section class="card card--back" aria-label="Back of business card">
    <div class="brand">
      <span class="brand__mark"></span>
      <span class="brand__name">Brisk Grout Studio</span>
    </div>
    <div class="pitch">
      <p class="pitch__quote">"Quality tile installation at an affordable price"</p>
      <p class="pitch__line">Residential &amp; Commercial ~ Free Estimates</p>
      <p class="pitch__web">briskgroutstudio.net</p>
    </div>
  </section>
</main>
</body>
</html>
```